Icon-Design für Entwicklung von IT-Anwendungen
Zielgruppe
Entwicklung von IT-Anwendungen - Schwerpunkt sind Intranet-Anwendungen
Aufgabenstellung
Modernes Button-Layout mit Fokus auf 'technisches', eher schnörkelloses Design
1. Gewünscht wird ein modernes Layout für 8 Buttons (vgl. alte Buttons in buttons.png). Für jede Aktion (z.B. Einzelprojekt bearbeiten, Speichern, Löschen, usw.) soll ein aussagefähiges Icon und der jeweilige Text enthalten sein.
2. Für jeden Button soll es eine Highlight-Variante geben (für spätere MouseOver-Anwendung)
3. Weiterhin wird eine Leiste gewünscht, in die die Buttons später integriert werden. Als Farbe soll ein Blauton verwendet werden, der zum restlichen Blau harmoniert.
Technische Vorgaben für Buttons
- Größe jeweils 130 x 34 Pixel
- Hintergrundfarbe transparent
- Photoshop-Dateiformat, so dass Texte editierbar bleiben
Technische Vorgaben für Leiste
- Größe 1320 x 40 Pixel
- PNG-Dateiformat

```html
<!DOCTYPE html>
<html lang="de">
<head>
<meta charset="utf-8">
<title>Button-Leiste Projektverwaltung</title>
<link rel="stylesheet" href="https://fonts.googleapis.com/css2?family=PT+Sans:wght@400;700&display=swap">
<style>
  :root {
    --page-bg: #ffffff;
    --bar-top: #dadada;
    --bar-bottom: #c3c3c3;
    --divider-light: #e6e6e6;
    --divider-dark: #b8b8b8;
    --action-blue: #2a6fd6;
    --hover-blue-top: #2161b8;
    --hover-blue-bottom: #0c3d80;
    --hover-red-top: #ee1111;
    --hover-red-bottom: #a80000;
    --hover-text: #ffffff;
    --heading-grey: #a9a9a9;
  }
  * { margin: 0; padding: 0; box-sizing: border-box; }
  html, body { width: 1200px; height: 416px; overflow: hidden; background: var(--page-bg); }
  body { position: relative; font-family: "PT Sans", sans-serif; }

  .toolbar {
    position: absolute;
    left: 95px;
    width: 1011px;
    height: 26px;
    display: grid;
    grid-template-columns: repeat(8, 1fr);
    background: linear-gradient(var(--bar-top), var(--bar-bottom));
    box-shadow: 0 2px 3px rgba(0,0,0,0.28);
  }
  .toolbar--default { top: 67px; }
  .toolbar--hover-delete { top: 251px; }
  .toolbar--hover-view { top: 315px; }

  .action {
    position: relative;
    display: flex;
    align-items: center;
    color: var(--action-blue);
    font-size: 8.2px;
    line-height: 9.6px;
    border-left: 1px solid var(--divider-light);
    border-right: 1px solid var(--divider-dark);
  }
  .action:first-child { border-left: 0; }
  .action:last-child { border-right: 0; }
  .action__icon {
    position: absolute;
    left: 8px;
    top: 4px;
    width: 24px;
    height: 18px;
    fill: currentColor;
  }
  .action__label { margin-left: 46px; }

  .action--danger-active {
    background: linear-gradient(var(--hover-red-top), var(--hover-red-bottom));
    color: var(--hover-text);
  }
  .action--primary-active {
    background: linear-gradient(var(--hover-blue-top), var(--hover-blue-bottom));
    color: var(--hover-text);
  }

  .section-title {
    position: absolute;
    left: 95px;
    top: 205px;
    font-size: 22px;
    font-weight: 700;
    color: var(--heading-grey);
  }

  .pointer { position: absolute; width: 24px; height: 30px; }
  .pointer--delete { left: 1087px; top: 266px; }
  .pointer--view { left: 326px; top: 333px; }
</style>
</head>
<body>

<svg width="0" height="0" style="position:absolute">
  <defs>
    <symbol id="icon-new" viewBox="0 0 24 18">
      <path d="M1 4h6l2 2h8v3H5L2 16z"/><path d="M4 9h14l-3 8H1z"/>
      <path d="M18 2h2v3h3v2h-3v3h-2V7h-3V5h3z"/>
    </symbol>
    <symbol id="icon-single" viewBox="0 0 24 18">
      <path d="M3 4h6v13H6l-3-3z"/><circle cx="13" cy="7" r="5"/>
      <circle cx="13" cy="7" r="3" fill="#d2d2d2"/><path d="M16 10l3 4-2 1-3-4z"/>
    </symbol>
    <symbol id="icon-multi" viewBox="0 0 24 18">
      <path d="M1 4h6l2 2h5v10H3z"/><path d="M4 8h10l-2 9H1z"/>
      <circle cx="16" cy="7" r="5"/><circle cx="16" cy="7" r="3" fill="#d2d2d2"/>
      <path d="M19 10l3 4-2 1-3-4z"/>
    </symbol>
    <symbol id="icon-edit" viewBox="0 0 24 18">
      <path d="M9 2l9 9-5 6-9-9z"/><path d="M4 9l8 8H5l-3-3z"/>
      <path d="M14 2l3-1 4 4-1 3z"/>
    </symbol>
    <symbol id="icon-save-prev" viewBox="0 0 24 18">
      <path d="M3 1h13l3 3v6h-5v7H3z"/><rect x="7" y="1" width="6" height="4" fill="#d2d2d2"/>
      <path d="M15 13c0-3 3-4 6-3v-2l3 3-3 3v-2c-2 0-4 0-4 3z" transform="matrix(-1 0 0 1 38 0)"/>
    </symbol>
    <symbol id="icon-save-next" viewBox="0 0 24 18">
      <path d="M3 1h13l3 3v6h-5v7H3z"/><rect x="7" y="1" width="6" height="4" fill="#d2d2d2"/>
      <path d="M15 15c0-3 2-5 5-5v-2l3 3-3 3v-2c-2 0-3 1-5 3z"/>
    </symbol>
    <symbol id="icon-duplicate" viewBox="0 0 24 18">
      <path d="M2 3h6l2 2h10v3H4z"/><path d="M1 8h21l-2 9H3z"/>
      <path d="M4 6h18v1H4z"/>
    </symbol>
    <symbol id="icon-delete" viewBox="0 0 24 18">
      <path d="M6 3h12v2H6z"/><path d="M10 1h4v2h-4z"/>
      <path d="M7 6h10l-1 11H8zM9.5 8v7h1.2V8zm3.8 0v7h1.2V8z" fill-rule="evenodd"/>
    </symbol>
    <symbol id="cursor-arrow" viewBox="0 0 24 30">
      <path d="M1 1v22l6-5 4 9 4-2-4-8h8z" fill="#fff" stroke="#000" stroke-width="2" stroke-linejoin="round"/>
    </symbol>
  </defs>
</svg>

<nav class="toolbar toolbar--default" aria-label="Projektaktionen">
  <div class="action"><svg class="action__icon"><use href="#icon-new"/></svg><span class="action__label">Neues Projekt<br>anlegen</span></div>
  <div class="action"><svg class="action__icon"><use href="#icon-single"/></svg><span class="action__label">Einzelprojektansicht</span></div>
  <div class="action"><svg class="action__icon"><use href="#icon-multi"/></svg><span class="action__label">Multiprojektansicht</span></div>
  <div class="action"><svg class="action__icon"><use href="#icon-edit"/></svg><span class="action__label">Einzelprojekt<br>bearbeiten</span></div>
  <div class="action"><svg class="action__icon"><use href="#icon-save-prev"/></svg><span class="action__label">Speichern und zum<br>letzten Projekt</span></div>
  <div class="action"><svg class="action__icon"><use href="#icon-save-next"/></svg><span class="action__label">Speichern und zum<br>nächsten Projekt</span></div>
  <div class="action"><svg class="action__icon"><use href="#icon-duplicate"/></svg><span class="action__label">Dupliziere<br>dieses Projekt</span></div>
  <div class="action"><svg class="action__icon"><use href="#icon-delete"/></svg><span class="action__label">Lösche dieses Projekt</span></div>
</nav>

<h2 class="section-title">Rollover-Effekte:</h2>

<nav class="toolbar toolbar--hover-delete" aria-label="Projektaktionen, Löschen hervorgehoben">
  <div class="action"><svg class="action__icon"><use href="#icon-new"/></svg><span class="action__label">Neues Projekt<br>anlegen</span></div>
  <div class="action"><svg class="action__icon"><use href="#icon-single"/></svg><span class="action__label">Einzelprojektansicht</span></div>
  <div class="action"><svg class="action__icon"><use href="#icon-multi"/></svg><span class="action__label">Multiprojektansicht</span></div>
  <div class="action"><svg class="action__icon"><use href="#icon-edit"/></svg><span class="action__label">Einzelprojekt<br>bearbeiten</span></div>
  <div class="action"><svg class="action__icon"><use href="#icon-save-prev"/></svg><span class="action__label">Speichern und zum<br>letzten Projekt</span></div>
  <div class="action"><svg class="action__icon"><use href="#icon-save-next"/></svg><span class="action__label">Speichern und zum<br>nächsten Projekt</span></div>
  <div class="action"><svg class="action__icon"><use href="#icon-duplicate"/></svg><span class="action__label">Dupliziere<br>dieses Projekt</span></div>
  <div class="action action--danger-active"><svg class="action__icon"><use href="#icon-delete"/></svg><span class="action__label">Lösche dieses Projekt</span></div>
</nav>
<svg class="pointer pointer--delete" aria-hidden="true"><use href="#cursor-arrow"/></svg>

<nav class="toolbar toolbar--hover-view" aria-label="Projektaktionen, Einzelprojektansicht hervorgehoben">
  <div class="action"><svg class="action__icon"><use href="#icon-new"/></svg><span class="action__label">Neues Projekt<br>anlegen</span></div>
  <div class="action action--primary-active"><svg class="action__icon"><use href="#icon-single"/></svg><span class="action__label">Einzelprojektansicht</span></div>
  <div class="action"><svg class="action__icon"><use href="#icon-multi"/></svg><span class="action__label">Multiprojektansicht</span></div>
  <div class="action"><svg class="action__icon"><use href="#icon-edit"/></svg><span class="action__label">Einzelprojekt<br>bearbeiten</span></div>
  <div class="action"><svg class="action__icon"><use href="#icon-save-prev"/></svg><span class="action__label">Speichern und zum<br>letzten Projekt</span></div>
  <div class="action"><svg class="action__icon"><use href="#icon-save-next"/></svg><span class="action__label">Speichern und zum<br>nächsten Projekt</span></div>
  <div class="action"><svg class="action__icon"><use href="#icon-duplicate"/></svg><span class="action__label">Dupliziere<br>dieses Projekt</span></div>
  <div class="action"><svg class="action__icon"><use href="#icon-delete"/></svg><span class="action__label">Lösche dieses Projekt</span></div>
</nav>
<svg class="pointer pointer--view" aria-hidden="true"><use href="#cursor-arrow"/></svg>

</body>
</html>
```